Cover für den Roman Marlene betritt die Bühne
Zielgruppe
Autorin einer belletristischen Erzählung über die Kunst der Moderne. Das Buch richtet sich an Leser die sich für Moderne Kunst interessieren.
Aufgabenstellung
Gesucht wird ein sehr zeitgemäßes und auffallendes Design, auch gerne mit einer starken Hintergrundfarbe. Der Leser soll auf den ersten Blick erkennen können, dass es hier um Kunst geht (Lorenz Aubach, Tarnowski, Ferrandi Hadley, etc). Bitte unbedingt alle Lizenzrechte abklären und keine Originalwerke verwenden.
Eine Idee wäre einen Bezug zu "Marlene und der Barastides" herzustellen. (Vielzitiertes Thema in der Kunstgeschichte, Marlene schlägt dem Feldherrn Barastides den Kopf ab und befreit ihr Volk.)
Das Design sollte aber trotzdem nett und nicht gruselig sein.
Ganz wichtig keine nackte Marlene. Sie ist stark und emanzipiert sich!
Text auf der Vorderseite:
Olga Mertelhuber
Marlene betritt die Bühne
Erzählung über die Kunst der Moderne
Text auf der Rückseite:
kurze Inhaltsangabe
Das Cover soll für ein Taschenbuch als auch ein e-book funktionieren

```html
<!DOCTYPE html>
<html lang="de">
<head>
<meta charset="utf-8">
<title>Marlene betritt die Bühne – Rückseite</title>
<link href="https://fonts.googleapis.com/css2?family=Monsieur+La+Doulaise&family=Tinos&display=swap" rel="stylesheet">
<style>
  :root {
    --red-deep: #a5000f;
    --red-mid: #b51822;
    --red-light: #c23a3f;
    --red-shadow: #8e0410;
    --text: #ffffff;
  }
  html, body {
    margin: 0;
    padding: 0;
    width: 840px;
    height: 1200px;
    overflow: hidden;
    background: var(--red-deep);
  }
  .back-cover {
    position: relative;
    width: 840px;
    height: 1200px;
    overflow: hidden;
  }
  .painted-figure {
    position: absolute;
    inset: 0;
    background:
      radial-gradient(ellipse 32% 60% at 44% 52%, var(--red-light) 0%, rgba(194,58,63,0) 70%),
      radial-gradient(ellipse 80% 70% at 55% 40%, var(--red-mid) 0%, var(--red-deep) 75%),
      linear-gradient(180deg, var(--red-mid) 0%, var(--red-shadow) 100%);
  }
  .title {
    position: absolute;
    top: 285px;
    left: 0;
    width: 840px;
    margin: 0;
    text-align: center;
    font-family: "Monsieur La Doulaise", cursive;
    font-weight: 400;
    font-size: 78px;
    line-height: 1;
    color: var(--text);
    white-space: nowrap;
  }
  .synopsis {
    position: absolute;
    top: 404px;
    left: 120px;
    width: 600px;
    margin: 0;
    text-align: center;
    font-family: "Tinos", "Times New Roman", serif;
    font-size: 22px;
    line-height: 38px;
    color: var(--text);
  }
  .synopsis span { display: block; white-space: nowrap; }
</style>
</head>
<body>
<main class="back-cover">
  <div class="painted-figure" role="img" aria-label="Gemalte, in Rottönen aufgelöste Figur einer Frau, die den ganzen Hintergrund füllt"></div>
  <h1 class="title">Marlene betritt die Bühne</h1>
  <p class="synopsis">
    <span>Marlene und Cornelius treffen zufällig</span>
    <span>aufeinander und beginnen ein Gespräch über die</span>
    <span>Kunst der Moderne. Der Leser erfährt alles</span>
    <span>Wissenswerte über die Kunst der letzten 120 Jahre.</span>
    <span>Wie die Fotografie eine neue Malerei notwendig</span>
    <span>machte, wie die Erfindung der Farbtube den</span>
    <span>Impressionismus ermöglicht hat oder was neue</span>
    <span>Musik und Oliven gemeinsam haben.</span>
    <span>Am Ende darf Marlene ihrem Namen auch noch</span>
    <span>gerecht werden und schlägt dem belehrenden</span>
    <span>alten Mann den Kopf ab. So gewinnt die</span>
    <span>Emanzipation von alten Rollenmustern doch noch</span>
    <span>die Oberhand, ganz im Sinne der Moderne.</span>
  </p>
</main>
</body>
</html>
```